I need an amazing business card!

I am the principle in my own software company that develops vexPad and mobile applications. I require a great business card design. I've attached my corporate logo (Thanks Tomasz!).
I would like the design to integrate the logo, my name, email address and skype account:
name Brent Halloway
email brenthalloway@zelqor.com
skype brenthalloway.net
I would like the back of the card to have a "write on me area" similar to the "write on me" card on this page, row 6:
http://us.pravik.com/design-templates/business-cards/#industry=Computing%20%26%20IT
As far as the rest - it's all you!
Updates
1) Please add an example telephone number as well.
Industry/Entity Type
Software
Look and feel
Each slider illustrates characteristics of the customer's brand and the style your logo design should communicate.

```html
<!DOCTYPE html>
<html lang="en">
<head>
<meta charset="utf-8">
<title>Brent Halloway – Business Card</title>
<link rel="stylesheet" href="https://fonts.googleapis.com/css2?family=Carlito&family=Tinos:ital@1&display=swap">
<style>
  :root {
    --backdrop: #c4c4c4;
    --card: #232323;
    --screen: #2e2e2e;
    --screen-back: #333333;
    --frame-front: #4a4a4a;
    --frame-back: #1a1a1a;
    --button: #1b1b1b;
    --button-edge: #3c3c3c;
    --text: #ffffff;
    --rule: #a8a8a8;
    --tag: #ffffff;
    --brand: #8cb43a;
    --write-line: #f9f9fb;
  }
  * { margin: 0; padding: 0; box-sizing: border-box; }
  html, body {
    width: 1200px;
    height: 894px;
    overflow: hidden;
    background: var(--backdrop);
  }
  .canvas {
    position: relative;
    width: 1200px;
    height: 894px;
  }
  .card {
    position: absolute;
    left: 284px;
    width: 634px;
    height: 386px;
    background: var(--card);
  }
  .card--front { top: 32px; }
  .card--back { top: 467px; }
  .card__device {
    position: absolute;
    inset: 0;
  }
  .card__name {
    position: absolute;
    left: 82px;
    top: 108px;
    max-width: 340px;
    white-space: nowrap;
    font-family: "Tinos", "Times New Roman", serif;
    font-style: italic;
    font-weight: 400;
    font-size: 48px;
    line-height: 1;
    color: var(--text);
  }
  .card__rule {
    position: absolute;
    left: 83px;
    top: 208px;
    width: 404px;
    height: 1px;
    background: var(--rule);
  }
  .card__contact {
    position: absolute;
    left: 83px;
    top: 225px;
    list-style: none;
    font-family: "Carlito", "Calibri", sans-serif;
    font-size: 23px;
    line-height: 31.5px;
    color: var(--text);
  }
  .brand-tag {
    position: absolute;
    z-index: 2;
    left: 432px;
    top: 32px;
    width: 107px;
    height: 124px;
    background: var(--tag);
    clip-path: polygon(0 0, 100% 0, 100% 84%, 50% 100%, 0 84%);
    display: flex;
    flex-direction: column;
    align-items: center;
    padding-top: 13px;
    gap: 6px;
  }
  .brand-tag__mark {
    width: 56px;
    height: 56px;
    border-radius: 12px;
    background: var(--brand);
  }
  .brand-tag__name {
    font-family: "Carlito", "Calibri", sans-serif;
    font-size: 17px;
    line-height: 1;
    letter-spacing: 4px;
    padding-left: 4px;
    color: var(--brand);
  }
</style>
</head>
<body>
<main class="canvas">
  <section class="card card--front" aria-label="Business card front">
    <svg class="card__device" width="634" height="386" viewBox="0 0 634 386" aria-hidden="true">
      <rect x="21" y="29" width="585" height="337" rx="46" fill="none" stroke="var(--frame-front)" stroke-width="3"/>
      <rect x="66" y="68" width="437" height="261" fill="var(--screen)"/>
      <rect x="45" y="168" width="9" height="60" rx="4" fill="var(--card)" stroke="var(--button-edge)" stroke-width="2"/>
      <circle cx="546" cy="197" r="32" fill="var(--button)" stroke="var(--button-edge)" stroke-width="2"/>
      <rect x="535" y="186" width="22" height="22" rx="2" fill="none" stroke="var(--button-edge)" stroke-width="2"/>
    </svg>
    <h1 class="card__name">Brent Halloway</h1>
    <div class="card__rule"></div>
    <ul class="card__contact">
      <li>email: brenthalloway@zelqor.com</li>
      <li>skype: brenthalloway.net</li>
      <li>tel: 0352 481 706</li>
    </ul>
    <div class="brand-tag">
      <span class="brand-tag__mark"></span>
      <span class="brand-tag__name">zelqor</span>
    </div>
  </section>

  <section class="card card--back" aria-label="Business card back with write-on area">
    <svg class="card__device" width="634" height="386" viewBox="0 0 634 386" aria-hidden="true">
      <rect x="26" y="30" width="578" height="335" rx="46" fill="none" stroke="var(--frame-back)" stroke-width="3"/>
      <rect x="68" y="68" width="436" height="262" fill="var(--screen-back)"/>
      <rect x="47" y="169" width="9" height="58" rx="4" fill="var(--card)" stroke="var(--button-edge)" stroke-width="2"/>
      <circle cx="548" cy="198" r="32" fill="var(--button)" stroke="var(--button-edge)" stroke-width="2"/>
      <rect x="537" y="187" width="22" height="22" rx="2" fill="none" stroke="var(--button-edge)" stroke-width="2"/>
      <g class="write-lines" fill="var(--write-line)">
        <rect x="91" y="97" width="389" height="38"/>
        <rect x="91" y="154" width="389" height="38"/>
        <rect x="91" y="212" width="389" height="38"/>
        <rect x="91" y="267" width="389" height="38"/>
      </g>
    </svg>
  </section>
</main>
</body>
</html>
```